Design some Business Cards

Thank you so much for viewing my contest ! Please be creative
I need some business cards with a cool design, simple and professional.
Below i will add 2 Logos. I want a matte black Background Entry, and a white background entry both front and back. PLEASE KEEP ORIGINAL LOGO COLORS
Please add to the back of the card
Service/Repair/Installations
Duct cleaning services
Miami Dade/Broward County
Call now for a free quote
Special Duct Cleaning Prices
I will need to include contact info for example:
Instagram
Email
Phone Number
Thank you any questions feel free to contact me.!
I appreciate any creative work!

```html
<!DOCTYPE html>
<html lang="en">
<head>
<meta charset="utf-8">
<title>Coolcrest Air Business Cards</title>
<link href="https://fonts.googleapis.com/css2?family=Lato:wght@400;700;900&display=swap" rel="stylesheet">
<style>
  :root {
    --bg: #e4e6ea;
    --card: #ffffff;
    --brand-blue: #1e77a6;
    --brand-red: #d2262e;
    --ink: #1d1d1f;
    --rule: #c9ccd2;
  }
  * { box-sizing: border-box; margin: 0; padding: 0; }
  html, body { width: 1200px; height: 900px; overflow: hidden; }
  body {
    background: var(--bg);
    font-family: "Lato", sans-serif;
    display: flex;
    flex-direction: column;
    align-items: center;
    justify-content: center;
    gap: 56px;
  }
  .card {
    position: relative;
    width: 620px;
    height: 354px;
    background: var(--card);
    border-radius: 24px;
    overflow: hidden;
    box-shadow: 0 10px 30px rgba(0,0,0,.12);
  }
  .brand {
    display: flex;
    align-items: center;
    gap: 14px;
    color: var(--brand-blue);
    font-weight: 900;
    letter-spacing: .02em;
    text-transform: uppercase;
  }
  .brand-dot {
    border: 4px solid var(--brand-blue);
    border-radius: 50%;
    flex: none;
  }
  /* back */
  .card-back { display: flex; align-items: center; justify-content: center; }
  .card-back .brand { font-size: 40px; }
  .card-back .brand-dot { width: 62px; height: 62px; }
  /* front */
  .front-art { position: absolute; inset: 0; }
  .card-front .brand { position: absolute; left: 40px; top: 58px; font-size: 22px; gap: 10px; }
  .card-front .brand-dot { width: 34px; height: 34px; border-width: 3px; }
  .holder { position: absolute; left: 352px; top: 92px; }
  .holder-name { font-size: 26px; font-weight: 400; color: var(--ink); letter-spacing: .04em; }
  .holder-role { font-size: 16px; color: var(--ink); margin-top: 2px; }
  .holder-role span { color: var(--brand-blue); }
  .contacts {
    position: absolute; left: 312px; top: 170px;
    list-style: none;
    border-left: 1px solid var(--rule);
    padding-left: 14px;
    display: flex; flex-direction: column; gap: 9px;
  }
  .contacts li { display: flex; align-items: center; gap: 12px; font-size: 16px; color: var(--ink); }
  .contact-icon {
    width: 22px; height: 22px; border-radius: 4px;
    background: var(--brand-red);
    display: flex; align-items: center; justify-content: center; flex: none;
  }
  .contact-icon svg { width: 14px; height: 14px; fill: #fff; }
</style>
</head>
<body>

<section class="card card-back" aria-label="Card back">
  <div class="brand"><span class="brand-dot"></span>Coolcrest Air</div>
</section>

<section class="card card-front" aria-label="Card front">
  <svg class="front-art" viewBox="0 0 620 354" aria-hidden="true">
    <path d="M0,160 C150,175 330,250 470,354 L0,354 Z" fill="var(--brand-blue)"/>
    <path d="M0,132 C110,134 200,150 270,182 C200,156 110,142 0,140 Z" fill="var(--brand-red)"/>
  </svg>

  <div class="brand"><span class="brand-dot"></span>Coolcrest Air</div>

  <div class="holder">
    <p class="holder-name">Sam Rivera</p>
    <p class="holder-role">Operations <span>Manager</span></p>
  </div>

  <ul class="contacts">
    <li><span class="contact-icon"><svg viewBox="0 0 24 24"><path d="M6.6 10.8a15.1 15.1 0 0 0 6.6 6.6l2.2-2.2a1 1 0 0 1 1-.25 11.4 11.4 0 0 0 3.6.57 1 1 0 0 1 1 1V20a1 1 0 0 1-1 1A17 17 0 0 1 3 4a1 1 0 0 1 1-1h3.5a1 1 0 0 1 1 1c0 1.25.2 2.45.57 3.57a1 1 0 0 1-.25 1z"/></svg></span>+432.555.0147</li>
    <li><span class="contact-icon"><svg viewBox="0 0 24 24"><rect x="5" y="5" width="14" height="14" rx="2"/></svg></span>@coolcrestair</li>
    <li><span class="contact-icon"><svg viewBox="0 0 24 24"><path d="M3 6h18v12H3z M3 6l9 7 9-7" fill="none" stroke="#fff" stroke-width="2"/></svg></span>hello@coolcrestair.com</li>
    <li><span class="contact-icon"><svg viewBox="0 0 24 24"><path d="M12 2a7 7 0 0 0-7 7c0 5 7 13 7 13s7-8 7-13a7 7 0 0 0-7-7zm0 9.5A2.5 2.5 0 1 1 12 6.5a2.5 2.5 0 0 1 0 5z"/></svg></span>27 Harbor Lane, Miami</li>
  </ul>
</section>

</body>
</html>
```